Brackwell Advisory - WorkNexa Header

I am a solopreneur with a consulting company. I do management consulting for small and mid-size manufacturers. There are two ways my prospects check me out - my web page, which went live this week (www.brackwelladvisory.com), and my personal WorkNexa page. I'm working on my WorkNexa page now, and I'd like to have a header image that is unique and aligned with my brand.

My clients are smaller manufacturers, typically with 50-400 people. They are privately held, often by an individual or family, but sometimes by a professional investment group. They aren't as sophisticated as the Meridian 250 guys, and sometimes they struggle to grow because their processes break, or they don't have the right people or something else like that. I help them get through those issues.

Many of the people visiting the site will have a technical/engineering orientation, and most are in their late 40's to early 60's.

From my research, I think the image for my personal page is 1584x396, and this will be my primary page. The business page has a banner image size of 1536x768. I'd like to be able to use the same image in both.

Target Market(s)

Small and Mid-size manufacturers - C-Suite executives

Industry/Entity Type

Manufacturing

Font styles to use
Sans Serif

Colors

Designer to choose colors to be used in the design.

Requirements
Must have
• Logo incorporated. Be adaptable to both my personal WorkNexa page and Business page, which have slightly different sizes.

```html
<!DOCTYPE html>
<html lang="en">
<head>
<meta charset="utf-8">
<title>Brackwell Advisory – WorkNexa Header</title>
<link rel="stylesheet" href="https://fonts.googleapis.com/css2?family=Titillium+Web:wght@300;600;700&display=swap">
<style>
  :root {
    --page-bg: #0a0f1f;
    --night: #0b0f17;
    --night-soft: #121a28;
    --paper: #ffffff;
    --brand-navy: #0a1a8c;
    --brand-orange: #f7982e;
    --quote-navy: #14206e;
    --mark-grey: #5f6366;
  }
  * { margin: 0; padding: 0; box-sizing: border-box; }
  html, body {
    width: 1200px; height: 1200px; overflow: hidden;
    background: var(--page-bg);
    font-family: "Titillium Web", sans-serif;
  }
  .canvas { position: relative; width: 1200px; height: 1200px; }
  .banner { position: absolute; left: 0; width: 1200px; overflow: hidden; }
  .banner--dark { top: 242px; height: 300px; }
  .banner--color { top: 659px; height: 299px; }
  .banner__shapes { position: absolute; inset: 0; }
  .brand {
    position: absolute; left: 16px; top: 20px;
    display: flex; align-items: center; gap: 12px;
  }
  .brand__dot {
    width: 44px; height: 44px; border-radius: 50%;
    background: var(--brand-navy);
  }
  .brand__name {
    font-weight: 600; font-size: 25px; color: var(--brand-navy);
    letter-spacing: 0.2px;
  }
  .testimonial {
    position: absolute; right: 50px; top: 50px;
    text-align: right;
  }
  .testimonial__quote {
    font-weight: 300; font-size: 23.5px; line-height: 31px;
    letter-spacing: 0.3px;
  }
  .testimonial__author {
    margin-top: 14px;
    font-weight: 700; font-size: 19.5px; line-height: 25px;
    text-transform: uppercase; letter-spacing: 0.5px;
    color: var(--paper);
  }
  .banner--dark .testimonial__quote { color: var(--paper); }
  .banner--color .testimonial__quote { color: var(--quote-navy); }
</style>
</head>
<body>
<div class="canvas">

  <section class="banner banner--dark">
    <svg class="banner__shapes" width="1200" height="300" viewBox="0 0 1200 300">
      <defs>
        <linearGradient id="night-sheen" x1="0" y1="0" x2="1" y2="1">
          <stop offset="0" stop-color="var(--night-soft)"/>
          <stop offset="1" stop-color="var(--night)"/>
        </linearGradient>
      </defs>
      <rect width="1200" height="300" fill="var(--night)"/>
      <polygon points="230,95 1200,0 1200,300 1090,300" fill="url(#night-sheen)" opacity="0.8"/>
      <polygon points="0,0 565,0 0,136" fill="var(--paper)"/>
    </svg>
    <div class="brand">
      <span class="brand__dot"></span>
      <span class="brand__name">Brackwell Advisory</span>
    </div>
    <blockquote class="testimonial">
      <p class="testimonial__quote">“Ken was a tremendous help to our leadership team.<br>
      He was able to quickly identify some of our underlying challenges,<br>
      and he helped us fill those gaps with some practical management tools.<br>
      We saw immediate results, and those improvements<br>
      have stuck with us to this day.”</p>
      <p class="testimonial__author">Martin Hallberg<br>CEO, Stratalabel</p>
    </blockquote>
  </section>

  <section class="banner banner--color">
    <svg class="banner__shapes" width="1200" height="299" viewBox="0 0 1200 299">
      <rect width="1200" height="299" fill="var(--brand-orange)"/>
      <polygon points="568,0 1200,0 1200,32" fill="var(--brand-navy)"/>
      <polygon points="0,137 335,57 243,299 0,299" fill="var(--brand-navy)"/>
      <polygon points="0,0 568,0 0,137" fill="var(--paper)"/>
    </svg>
    <div class="brand">
      <span class="brand__dot"></span>
      <span class="brand__name">Brackwell Advisory</span>
    </div>
    <blockquote class="testimonial">
      <p class="testimonial__quote">“Ken was a tremendous help to our leadership team.<br>
      He was able to quickly identify some of our underlying challenges,<br>
      and he helped us fill those gaps with some practical management tools.<br>
      We saw immediate results, and those improvements<br>
      have stuck with us to this day.”</p>
      <p class="testimonial__author">Martin Hallberg<br>CEO, Stratalabel</p>
    </blockquote>
  </section>

</div>
</body>
</html>
```